Homes, Invest in Non-performing loans

We need only 3 web pages, one for the home, one for the content, one for the properties.
The main focus of our business is to offer non performing loans (before foreclosures) to the general public. All the non-performing mortgages will end in a house, an apartment, a store, etc.
Our customers are able to invest from 10,000usd to 1,000,000usd (average 50,000usd).
Our customers' usual focus groups are employees who want second earnings, perceiving the business feeling without outlay time. They look for a solid finance sense corporation that confers them certainty.
Nearly all our clients desire the house, apartment, store, etc. more than the actual earnings.
The name of our company is BRAMLEY
Reason: We value the time and effort you already invest in our project. We realize that we did't come back on some of the doubts requested by the designers. It will be inequitable to the designers who prerequisite our feedback. We also appreciate the comprehension of the community in this postponement.
Reason: Designers,
We really apreciate all the time and effort you put on our project. From the begining we ask for 3 pages, so now we will leave the 10 finalist and provide some extra time to submit the other 2 pages.
We will race the price in 10%
Target Market(s)
Our customers average investors works as employees and want to have a second income or business without spending time. (People from 35 to 50)
Industry/Entity Type
Finance
Requirements
Should not have
- FLASH

```html
<!DOCTYPE html>
<html lang="en">
<head>
<meta charset="utf-8">
<title>Bramley – Home</title>
<link rel="stylesheet" href="https://fonts.googleapis.com/css2?family=Source+Sans+3:wght@400;600;700&display=swap">
<style>
:root{
  --olive:#77722a;
  --olive-light:#e8e6a6;
  --ink:#3a3a3a;
  --muted:#555;
  --card:#7f7f7f;
  --footer:#27270b;
  --line:#bdbdbd;
  --white:#ffffff;
}
*{box-sizing:border-box;margin:0;padding:0}
html,body{width:1093px;height:1200px;overflow:hidden;background:var(--white)}
body{position:relative;font-family:"Source Sans 3",sans-serif;color:var(--ink)}
.brand{position:absolute;left:166px;top:62px;display:flex;align-items:center;gap:10px}
.brand-mark{width:26px;height:26px;background:var(--olive)}
.brand-name{font-size:32px;font-weight:700;color:#333;letter-spacing:1px}
.search{position:absolute;left:727px;top:28px;width:210px;height:41px;background:#f1f1f1;border:1px solid #ccc;border-top:2px solid #999;border-radius:3px;display:flex;align-items:center;padding:0 10px;font-size:16px;color:#666;justify-content:space-between}
.nav{position:absolute;left:569px;top:99px;display:flex;gap:0;font-size:15px;text-transform:uppercase}
.nav a{color:#333;text-decoration:none;height:37px;line-height:37px;padding:0 12px}
.nav a.active{background:var(--olive-light);border-radius:5px}
.hero{position:absolute;left:127px;top:150px;width:840px;height:441px;border:3px solid #f4f4f4;box-shadow:0 2px 8px rgba(0,0,0,.18);background:linear-gradient(90deg,#ffffff 0%,#f6f6f6 40%,#e6e6e6 70%,#d8d8d8 100%)}
.hero-photo{position:absolute;inset:0;background:radial-gradient(ellipse at 75% 55%,rgba(240,200,40,.55) 0,rgba(240,200,40,0) 18%),radial-gradient(ellipse at 65% 88%,rgba(190,160,90,.45) 0,rgba(190,160,90,0) 40%),radial-gradient(ellipse at 28% 30%,rgba(120,110,110,.35) 0,rgba(120,110,110,0) 28%)}
.hero-caption{position:absolute;left:30px;top:342px;font-size:18.5px;line-height:23px;color:#333}
.dots{position:absolute;left:506px;top:579px;width:97px;height:27px;background:#fff;border-radius:14px;box-shadow:0 2px 4px rgba(0,0,0,.25);display:flex;justify-content:center;align-items:center;gap:7px}
.dots span{width:12px;height:12px;border-radius:50%;border:1px solid #bbb;background:#f3f3f3}
.dots span.on{background:#ccc}
.welcome-title{position:absolute;left:126px;top:648px;width:840px;display:flex;align-items:center;gap:16px;font-size:17px;color:#333}
.welcome-title::before,.welcome-title::after{content:"";flex:1;height:1px;background:var(--line)}
.welcome-text{position:absolute;left:143px;top:684px;width:816px;text-align:center;font-size:12.3px;line-height:17.5px;color:var(--ink)}
.btn{position:absolute;height:23px;line-height:23px;padding:0 10px;background:var(--olive);color:#fff;font-size:13px;font-weight:600;border-radius:2px}
.card{position:absolute;top:802px;width:182px;height:112px;background:#fff;border:1px solid #ddd;box-shadow:0 0 3px rgba(0,0,0,.15);padding:2px}
.card-face{width:100%;height:100%;background:linear-gradient(160deg,#888 0%,#7b7b7b 60%,#727272 100%);display:flex;flex-direction:column;align-items:center;justify-content:flex-end;padding-bottom:10px;color:#fff;font-size:16px;font-weight:600;gap:4px}
.card-text{position:absolute;top:924px;width:182px;text-align:center;font-size:12.6px;line-height:17.5px;color:#444}
.skyline{position:absolute;left:0;top:1048px;width:1093px;height:84px;background:linear-gradient(180deg,rgba(160,160,140,0) 0%,#a4a48f 30%,#8e8e78 55%,#3d3d17 75%,var(--footer) 100%)}
.footer{position:absolute;left:0;top:1131px;width:1093px;height:69px;background:var(--footer);color:#eee;font-size:11px;text-align:center}
.footer p{margin-top:14px}
.social{display:flex;justify-content:center;gap:8px;margin-top:8px}
.social span{width:22px;height:22px;border-radius:50%;background:#7d7d70}
</style>
</head>
<body>
<div class="brand"><span class="brand-mark"></span><span class="brand-name">BRAMLEY</span></div>

<div class="search"><span>Search...</span>
<svg width="22" height="22" viewBox="0 0 22 22"><circle cx="9" cy="9" r="6.5" fill="none" stroke="#777" stroke-width="2"/><line x1="14" y1="14" x2="20" y2="20" stroke="#777" stroke-width="3" stroke-linecap="round"/></svg>
</div>

<nav class="nav"><a class="active" href="#">Home</a><a href="#">About Us</a><a href="#">Properties</a><a href="#">Contact Us</a></nav>

<section class="hero">
  <div class="hero-photo" role="img" aria-label="Group of investors beside a hand dropping a coin into a small yellow house among coin stacks"></div>
  <p class="hero-caption">Your second income or business<br>without spending time.</p>
</section>
<div class="dots"><span class="on"></span><span></span><span></span><span></span></div>

<h2 class="welcome-title">Welcome to our site</h2>
<p class="welcome-text">Lorem ipsum dolor sit amet, consectetur adipisicing elit, sed do eiusmod tempor incididunt ut labore et dolore magna aliqua. Ut enim ad minim veniam, quis nostrud exercitation ullamco laboris nisi ut aliquip ex ea commodo consequat. Duis aute irure dolor in reprehenderit in voluptate velit esse cillum dolore eu fugiat nulla pariatur. Excepteur sint occaecat cupidatat non proident, sunt in culpa qui officia deserunt mollit anim id est laborum.</p>
<span class="btn" style="left:529px;top:755px">More</span>

<div class="card" style="left:205px"><div class="card-face">
  <svg width="44" height="50" viewBox="0 0 44 50"><circle cx="22" cy="13" r="11" fill="#fff"/><path d="M2 50 V40 Q2 28 16 27 L22 38 L28 27 Q42 28 42 40 V50 Z" fill="#fff"/></svg>About Us</div></div>
<div class="card" style="left:459px"><div class="card-face">
  <svg width="56" height="50" viewBox="0 0 56 50"><path d="M28 3 L54 26 L49 30 L28 12 L7 30 L2 26 Z" fill="#fff"/><path d="M11 30 L28 16 L45 30 V49 H33 V36 H23 V49 H11 Z" fill="#fff"/></svg>Properties</div></div>
<div class="card" style="left:706px"><div class="card-face">
  <svg width="48" height="50" viewBox="0 0 48 50"><path d="M8 4 L16 2 L20 14 L14 18 Q18 30 30 34 L35 28 L46 33 L44 41 Q38 48 28 45 Q8 38 3 18 Q2 8 8 4 Z" fill="#fff"/></svg>Contact Us</div></div>

<p class="card-text" style="left:205px">Write here something your company details or about the brief here.</p>
<p class="card-text" style="left:459px">Write here something your company details or about the brief here.</p>
<p class="card-text" style="left:706px">Write here something your company details or about the brief here.</p>
<span class="btn" style="left:273px;top:991px">More</span>
<span class="btn" style="left:530px;top:991px">More</span>
<span class="btn" style="left:778px;top:991px">More</span>

<div class="skyline" role="img" aria-label="City skyline silhouette with houses"></div>
<footer class="footer">
  <p>Copyright @ 2014, Bramley &nbsp;|&nbsp; Terms &amp; Privacy Policy</p>
  <div class="social"><span></span><span></span></div>
</footer>
</body>
</html>
```